Postcard Design

www.tovil.com.au
i am an occupational therapist and professionally trained coach. i work with children, parents and disability service providers to achieve brilliant outcomes for children with special needs.
http://www.tovil.com.au/service/for-families
I need a postcard to give parents to promote our family service coaching service
A family service coach will work with you to set specific goals for your child, build a dream team, design and manage your child's highly effective therapy and educational team to ensure brilliant outcomes for your child..
KORBU - you have done my business card previously. they were great thank you.

```html
<!DOCTYPE html>
<html lang="en">
<head>
<meta charset="utf-8">
<title>Family Service Coaching – Postcard Front</title>
<link rel="stylesheet" href="https://fonts.googleapis.com/css2?family=Arimo:wght@700&family=Questrial&display=swap">
<style>
  :root {
    --brand-blue: #5a7bb6;
    --brand-blue-mid: #7d97c6;
    --brand-blue-light: #b3c3e0;
    --brand-blue-pale: #d6dfef;
    --text-slate: #5c6886;
    --paper: #ffffff;
    --photo-warm-1: #e9e1d6;
    --photo-warm-2: #c9ad92;
    --photo-warm-3: #8ea2bf;
  }
  * { margin: 0; padding: 0; box-sizing: border-box; }
  html, body {
    width: 1200px;
    height: 900px;
    overflow: hidden;
    background: var(--paper);
  }
  .postcard {
    position: relative;
    width: 1200px;
    height: 900px;
    background: var(--paper);
    overflow: hidden;
  }
  .postcard__graphics {
    position: absolute;
    inset: 0;
  }
  .brand {
    position: absolute;
    left: 62px;
    top: 78px;
    display: flex;
    align-items: center;
    gap: 16px;
    color: var(--paper);
    font-family: "Arimo", Arial, sans-serif;
    font-weight: 700;
    font-size: 58px;
    line-height: 1;
  }
  .brand__dot {
    width: 52px;
    height: 52px;
    border-radius: 50%;
    background: var(--paper);
  }
  .headline {
    position: absolute;
    left: 384px;
    top: 96px;
    font-family: "Arimo", Arial, sans-serif;
    font-weight: 700;
    font-size: 56px;
    line-height: 1;
    color: var(--brand-blue);
  }
  .intro {
    position: absolute;
    left: 160px;
    top: 268px;
    font-family: "Questrial", "Century Gothic", sans-serif;
    font-size: 35px;
    line-height: 44.5px;
    color: var(--text-slate);
  }
  .intro span { display: block; white-space: nowrap; }
  .intro .intro__spaced { letter-spacing: 0.42em; }
</style>
</head>
<body>
<main class="postcard">
  <svg class="postcard__graphics" width="1200" height="900" viewBox="0 0 1200 900" aria-hidden="false">
    <!-- corner disc -->
    <circle cx="110" cy="-70" r="345" fill="var(--brand-blue-light)"/>
    <circle cx="110" cy="-70" r="322" fill="var(--brand-blue)"/>

    <!-- guide lines -->
    <line x1="245" y1="220" x2="1022" y2="220" stroke="var(--brand-blue-mid)" stroke-width="2.5"/>
    <circle cx="1022" cy="220" r="9" fill="var(--brand-blue)"/>
    <circle cx="1022" cy="220" r="13" fill="none" stroke="var(--brand-blue-light)" stroke-width="3"/>
    <line x1="91" y1="250" x2="91" y2="818" stroke="var(--brand-blue-mid)" stroke-width="2.5"/>
    <circle cx="91" cy="818" r="9" fill="var(--brand-blue)"/>
    <circle cx="91" cy="818" r="13" fill="none" stroke="var(--brand-blue-light)" stroke-width="3"/>

    <!-- sweeping bands -->
    <path d="M 210 900 C 360 760, 470 560, 640 450 C 800 350, 1020 330, 1200 360 L 1200 900 Z" fill="var(--brand-blue-pale)"/>
    <path d="M 330 900 C 440 700, 560 500, 760 395 C 910 330, 1080 330, 1200 352 L 1200 900 Z" fill="var(--brand-blue-light)"/>
    <path d="M 420 900 C 500 700, 610 500, 800 405 C 940 345, 1090 345, 1200 365 L 1200 900 Z" fill="var(--brand-blue)"/>

    <!-- photo area -->
    <defs>
      <linearGradient id="photoTones" x1="0" y1="0" x2="1" y2="1">
        <stop offset="0" stop-color="var(--photo-warm-1)"/>
        <stop offset="0.55" stop-color="var(--photo-warm-2)"/>
        <stop offset="1" stop-color="var(--photo-warm-3)"/>
      </linearGradient>
    </defs>
    <path role="img" aria-label="Photo: a smiling family with a young child and a baby meeting with a family service coach at home"
          d="M 470 900 C 540 710, 640 520, 820 425 C 950 365, 1100 368, 1200 385 L 1200 900 Z"
          fill="url(#photoTones)"/>
  </svg>

  <div class="brand">
    <span class="brand__dot"></span>
    <span class="brand__name">tovil</span>
  </div>

  <h1 class="headline">Family Service Coaching</h1>

  <p class="intro">
    <span>A family service coach will work with</span>
    <span>you to set specific goals for your</span>
    <span>child, build a dream team,</span>
    <span>design&nbsp; and manage</span>
    <span>your child's&nbsp; highly</span>
    <span>effective therapy</span>
    <span>and educational</span>
    <span>team to ensure</span>
    <span class="intro__spaced">brilliant</span>
    <span>outcomes</span>
    <span>for your</span>
    <span>child..</span>
  </p>
</main>
</body>
</html>
```